Web design for boutique law firm

Web design for law firm; practice areas include:
-international intellectual property counseling
-general corporate (contract negotiation, licensing, distribution agreements
-see my *very* outdated website at www.pvtlegalhouse.com: here is some of the home page content:

"PVT Law Group enjoys providing proactive, business-minded, efficient legal solutions for individuals and companies that benefit from major law firm experience at reasonable rates.

Some areas of emphasis include:

Counseling individuals and companies with respect to clearing, selecting, securing, managing, commercializing, and protecting intellectual property assets around the world. This includes traditional global brand management, marketing, advertising, and enforcement work as well as litigation.
PVT Law Group also provides general counseling services for individuals and businesses, from start-up advice to sophisticated business transactions strategy, agreement negotiating, dispute resolution, and litigation.
Before founding PVT Law Group in 2008, Curtis L. Abernathy led the Trademark, Copyright, & Brand Management Group for Falkner & Ingleby's Seattle office. Curtis was also a senior associate at Silicon Valley based Hartwell, Bexley, Oduya, & Penrose."

Target Market(s)

Clients/potential clients needing tier one, international intellectual property advice with "mega" law firm experience for much less than what we were/would be charging at the "mega firms".

Industry/Entity Type

Legal

Number of Pages Required

4 page

Font styles to use
Serif
Sans Serif

Colors

Designer to choose colors to be used in the design.

Requirements
Must have
• +Improvement over everything on current site at www.pvtlegalhouse.com.
• +Pictures/bios for me and my team (four of us right now).
• +Easy to update and add/remove content.
• +Must be superior in design (look, feel, ease of use, classy and elegant, but hip, reflects international practice).
• +i have logos and color schemes (see current website) but will consider improvements.
Nice to have
• Let me know your thoughts.
Should not have
• No cheese; no overt sales pitches or marketing (since law firm).

```html
<!DOCTYPE html>
<html lang="en">
<head>
<meta charset="utf-8">
<title>PVT Law Group PLLC</title>
<link href="https://fonts.googleapis.com/css2?family=Lato:wght@300;400;700;900&family=Open+Sans:wght@400;600;700&display=swap" rel="stylesheet">
<style>
:root{
  --orange:#f26a12;
  --orange-light:#f47d2e;
  --ink:#111;
  --text:#555;
  --muted:#888;
  --grey-bg:#efefef;
  --soft-bg:#f4f4f4;
  --line:#ddd;
  --white:#fff;
}
*{margin:0;padding:0;box-sizing:border-box}
html,body{width:1200px;height:3468px;overflow:hidden;background:var(--white)}
body{font-family:"Open Sans",Arial,sans-serif;color:var(--text);position:relative}
section,header,footer{position:absolute;left:0;width:1200px}
.abs{position:absolute}

/* nav */
.site-header{top:0;height:69px;border-top:3px solid var(--orange);background:var(--white)}
.brand{left:173px;top:20px;font-family:"Lato",sans-serif;font-size:19px;font-weight:700;color:var(--orange)}
.nav{top:28px;font-family:"Lato",sans-serif;font-size:12px;color:#333;letter-spacing:.5px}
.nav.active::after{content:"";position:absolute;left:50%;top:20px;width:4px;height:4px;margin-left:-2px;border-radius:50%;background:var(--orange)}

/* hero */
.hero{top:69px;height:451px;background:linear-gradient(90deg,#cfcfcf 0%,#e6e6e6 35%,#f3f3f3 60%,#dcdcdc 100%)}
.hero-media{left:0;top:0;width:700px;height:451px;background:radial-gradient(ellipse at 35% 60%,#9a9a9a 0%,#c9c9c9 45%,transparent 75%)}
.hero-word{font-family:"Lato",sans-serif;font-weight:900;font-size:40px;color:var(--ink);letter-spacing:1px}
.hero-secure{left:767px;top:107px;width:262px;height:44px;background:var(--orange);color:var(--white);font-family:"Lato",sans-serif;font-weight:300;font-size:38px;text-align:center;line-height:44px;letter-spacing:2px}
.hero-copy{left:759px;top:226px;width:270px;text-align:right;font-size:11px;line-height:19px;color:#222;font-weight:600}

/* services band */
.services{top:520px;height:255px;display:flex}
.service{flex:1;position:relative;color:var(--white);text-align:center}
.service:first-child{background:var(--orange);flex:0 0 597px}
.service:last-child{background:var(--orange-light)}
.service svg{position:absolute;top:42px;left:50%;margin-left:-22px}
.service p{position:absolute;top:110px;left:50%;transform:translateX(-50%);width:420px;font-size:11px;line-height:19px}

/* who */
.who{top:775px;height:370px}
.section-title{font-family:"Lato",sans-serif;font-size:28px;color:var(--ink);font-weight:700;display:flex;align-items:center}
.section-title .bar{width:2px;height:34px;background:var(--orange);margin:0 14px}
.section-title .thin{font-weight:300;color:#555}
.who-copy{left:180px;top:138px;width:540px;font-size:11px;line-height:19px}
.btn-grey{left:180px;top:247px;width:125px;height:41px;background:#d8d8d8;font-size:10px;line-height:41px;text-align:center;color:#333;font-weight:600}
.portrait-frame{left:836px;top:86px;width:130px;height:156px;border:2px solid #555}
.portrait{left:825px;top:71px;width:130px;height:157px;background:linear-gradient(180deg,#d8d8d8,#7a7a7a)}

/* social links as text */
.social-links{display:flex;align-items:center;justify-content:center;font-family:"Open Sans",sans-serif;font-size:10px;font-weight:600;color:#222}
.social-links a{color:inherit;text-decoration:none}
.social-links .sep{width:1px;height:12px;background:#bbb;margin:0 9px}
.who-social{left:790px;top:276px;width:200px}

/* experience */
.experience{top:1145px;height:525px;background:var(--grey-bg)}
.exp-media{left:0;top:0;width:600px;height:525px;background:linear-gradient(120deg,#d6d6d6 0%,#f1f1f1 45%,#bdbdbd 100%)}
.exp-title{left:615px;top:80px}
.exp-sub{left:615px;top:155px;font-size:12px;font-weight:700;color:var(--ink)}
.exp-list{left:615px;top:190px;width:470px;font-size:11px;line-height:19px;list-style:none}
.btn-orange{background:var(--orange);color:var(--white);font-size:10px;text-align:center;font-weight:600}

/* blog */
.blog{top:1670px;height:650px}
.center-title{left:0;width:1200px;justify-content:center}
.lede{left:0;width:1200px;text-align:center;font-size:11px}
.post{top:198px;width:272px}
.post-media{width:272px;height:185px;position:relative}
.post-tag{position:absolute;left:0;bottom:0;width:40px;height:40px;background:var(--orange)}
.post h3{font-family:"Lato",sans-serif;font-size:17px;color:var(--ink);margin-top:30px;font-weight:700}
.post .meta{font-size:10px;color:var(--muted);margin-top:6px}
.post .meta b{color:var(--orange);font-weight:400}
.post p{font-size:11px;line-height:18px;margin-top:10px}
.dots{display:flex;gap:6px;left:586px}
.dots i{width:10px;height:10px;border-radius:50%;background:#bbb;display:block}
.dots i:last-child{background:var(--orange)}

/* testimonials */
.testimonials{top:2320px;height:651px;background:var(--soft-bg)}
.quote-card{top:184px;width:272px;height:365px;background:var(--white);text-align:center}
.avatar{width:80px;height:80px;border-radius:50%;margin:44px auto 0;background:linear-gradient(180deg,#b8b8b8,#6d6d6d)}
.quote-mark{font-family:"Lato",sans-serif;font-size:22px;color:#444;margin-top:8px;line-height:24px}
.quote-card p{font-size:11px;line-height:19px;width:210px;margin:28px auto 0}
.quote-card .name{color:var(--orange);font-size:11px;margin-top:10px}

/* cta */
.cta{top:2971px;height:139px;background:var(--orange);color:var(--white)}
.cta-title{left:180px;top:40px;font-family:"Lato",sans-serif;font-size:27px;display:flex;align-items:center}
.cta-title .bar{width:2px;height:34px;background:var(--white);margin:0 14px}
.cta-title .thin{font-weight:300}
.cta-copy{left:180px;top:91px;font-size:11px}
.btn-white{left:832px;top:48px;width:130px;height:40px;background:var(--white);color:#222;font-size:10px;font-weight:600;text-align:center;line-height:40px}

/* footer */
.site-footer{top:3110px;height:358px;background:linear-gradient(180deg,#fff 0%,#fafafa 40%,#e9e9e9 100%)}
.skyline{left:0;top:90px;width:1200px;height:268px;background:linear-gradient(180deg,rgba(200,200,200,0) 0%,rgba(190,190,190,.35) 100%)}
.f-name{left:384px;top:95px;font-family:"Lato",sans-serif;font-size:19px;color:var(--ink)}
.f-addr{left:384px;top:128px;font-size:10px;line-height:16px;color:#444}
.f-divider{left:601px;top:80px;width:1px;height:140px;background:#bbb}
.f-phone{left:689px;top:96px;font-size:17px;color:var(--ink);line-height:28px;font-weight:600}
.f-mail{left:689px;top:188px;font-size:15px;color:var(--ink);font-weight:600}
.f-rule{left:370px;top:235px;width:600px;height:1px;background:#ccc}
.f-social{left:500px;top:262px;width:200px}
.copyright{left:180px;top:327px;font-size:10px;color:#444}
.to-top{left:984px;top:300px;width:32px;height:32px;border:1.5px solid #333;border-radius:50%}
</style>
</head>
<body>

<header class="site-header">
  <div class="abs brand">PVT Law Group PLLC</div>
  <span class="abs nav active" style="left:622px">HOME</span>
  <span class="abs nav" style="left:703px">EXPERIENCE</span>
  <span class="abs nav" style="left:811px">SERVICES</span>
  <span class="abs nav" style="left:890px">ABOUT</span>
  <span class="abs nav" style="left:973px">CONTACT</span>
</header>

<section class="hero">
  <div class="abs hero-media" role="img" aria-label="Black and white chess pieces on a board"></div>
  <div class="abs hero-word" style="left:767px;top:56px">IMAGINE</div>
  <div class="abs hero-secure">SECURE</div>
  <div class="abs hero-word" style="left:767px;top:148px;width:262px;text-align:right">PROTECT</div>
  <p class="abs hero-copy">PVT Law Group enjoys providing proactive, business-minded, efficient legal solutions for individuals and companies that benefit from major law firm experience at reasonable rates.</p>
</section>

<section class="services">
  <div class="service">
    <svg width="44" height="46" viewBox="0 0 44 46" fill="none" stroke="#fff" stroke-width="1.6">
      <circle cx="16" cy="17" r="11"/><path d="M11 32h10M12 36h8M14 40h4"/><path d="M16 12v10M13 17h6"/>
      <path d="M27 17h8"/><circle cx="39" cy="17" r="3"/>
    </svg>
    <p>Counseling individuals and companies with respect to clearing, selecting, securing, managing, commercializing, and protecting intellectual property assets around the world. This includes traditional global brand management, marketing, advertising, and enforcement work as well as litigation.</p>
  </div>
  <div class="service">
    <svg width="44" height="46" viewBox="0 0 44 46" fill="none" stroke="#fff" stroke-width="1.6">
      <path d="M4 16L22 4l18 12z"/><rect x="8" y="18" width="28" height="20"/><path d="M4 42h36"/>
      <path d="M26 23h-6a2 2 0 000 5h4a2 2 0 010 5h-6M22 20v16"/>
    </svg>
    <p>PVT Law Group also provides general counseling services for individuals and businesses, from start-up advice to sophisticated business transactions strategy, agreement negotiating, dispute resolution, and litigation.</p>
  </div>
</section>

<section class="who">
  <h2 class="abs section-title" style="left:180px;top:74px">Who<span class="bar"></span><span class="thin">I am</span></h2>
  <p class="abs who-copy">Over the years, Curtis has worked with private and public companies in numerous industries, including consumer/retail products and services, various technology sectors (clean-technology, bio-tech, communications and networking, computer hardware and software, electronic), telecommunications, professional and educational services, among others.</p>
  <div class="abs btn-grey">READ MORE</div>
  <div class="abs portrait-frame"></div>
  <div class="abs portrait" role="img" aria-label="Portrait photo of the founding attorney"></div>
  <nav class="abs social-links who-social" aria-label="Social links">
    <a href="#">Share</a><span class="sep"></span><a href="#">Post</a><span class="sep"></span><a href="#">Plus</a><span class="sep"></span><a href="#">Connect</a>
  </nav>
</section>

<section class="experience">
  <div class="abs exp-media" role="img" aria-label="Reading glasses resting on an open book"></div>
  <h2 class="abs section-title exp-title">Experience<span class="bar"></span><span class="thin">Since 2008</span></h2>
  <div class="abs exp-sub">Professional/Community Involvement:</div>
  <ul class="abs exp-list">
    <li>Member, Global Brand Owners Association's (GBOA) Existing Content Evaluation Subcommittee for Information Resources Committee - 2010-2011 Term</li>
    <li>Member, Subcommittee for Information Resources Committee - 2008-2009 Term</li>
    <li>Member, GBOA since 2002</li>
    <li>Counseled pro-bono client, Riverside Hope Foundation, with branding strategies and entity formation, 2006</li>
    <li>Member, Business Development Sub-Committee, HarborTable, 2002-2003</li>
  </ul>
  <div class="abs btn-orange" style="left:615px;top:404px;width:127px;height:40px;line-height:40px">READ MORE</div>
</section>

<section class="blog">
  <h2 class="abs section-title center-title" style="top:62px">Blog<span class="bar"></span><span class="thin">Post</span></h2>
  <p class="abs lede" style="top:124px">Lorem ipsum dolor sit amet, consectetur adipiscing elit, sed do eiusmod tempor incididunt ut labore</p>

  <article class="abs post" style="left:169px">
    <div class="post-media" role="img" aria-label="Two people shaking hands over documents" style="background:linear-gradient(135deg,#e8e8e8,#b9b9b9)"><span class="post-tag"></span></div>
    <h3>Excepteur sint occaecat cupidata</h3>
    <div class="meta">by <b>admin</b> | Posted on 15 Apr</div>
    <p>Sed ut perspiciatis unde omnis iste natus error sit voluptatem accusantium doloremque laudantium, totam rem aperiam, eaque ipsa quae[...]</p>
  </article>
  <article class="abs post" style="left:464px">
    <div class="post-media" role="img" aria-label="Judge's gavel resting on a laptop keyboard" style="background:linear-gradient(135deg,#6f6f6f,#2f2f2f)"><span class="post-tag"></span></div>
    <h3>Architecto beatae vitae dicta</h3>
    <div class="meta">by <b>admin</b> | Posted on 07 Apr</div>
    <p>Sed ut perspiciatis unde omnis iste natus error sit voluptatem accusantium doloremque laudantium, totam rem aperiam, eaque ipsa quae[...]</p>
  </article>
  <article class="abs post" style="left:759px">
    <div class="post-media" role="img" aria-label="Hands reviewing a notebook with a pen" style="background:linear-gradient(135deg,#c9c4bd,#8a8580)"><span class="post-tag"></span></div>
    <h3>Excepteur sint occaecat cupidata</h3>
    <div class="meta">by <b>admin</b> | Posted on 25 Mar</div>
    <p>Sed ut perspiciatis unde omnis iste natus error sit voluptatem accusantium doloremque laudantium, totam rem aperiam, eaque ipsa quae[...]</p>
  </article>

  <div class="abs dots" style="top:588px"><i></i><i></i></div>
</section>

<section class="testimonials">
  <h2 class="abs section-title center-title" style="top:58px">Cleint<span class="bar"></span><span class="thin">Testimonials</span></h2>
  <p class="abs lede" style="top:122px">Lorem ipsum dolor sit amet, consectetur adipiscing elit, sed do eiusmod tempor incididunt ut labore</p>

  <div class="abs quote-card" style="left:169px">
    <div class="avatar" role="img" aria-label="Client portrait"></div>
    <div class="quote-mark">&#8220;</div>
    <p>Sed ut perspiciatis unde omnis iste natus error sit voluptatem accusantium dol ompue la ntuperiam, eaae</p>
    <div class="quote-mark" style="margin-top:16px">&#8221;</div>
    <div class="name">Dana Whitfield</div>
  </div>
  <div class="abs quote-card" style="left:464px">
    <div class="avatar" role="img" aria-label="Client portrait"></div>
    <div class="quote-mark">&#8220;</div>
    <p>Sed ut perspiciatis unde omnis iste natus error sit voluptatem accusantium dol ompue la ntuperiam, eaae</p>
    <div class="quote-mark" style="margin-top:16px">&#8221;</div>
    <div class="name">Lena Morrow</div>
  </div>
  <div class="abs quote-card" style="left:759px">
    <div class="avatar" role="img" aria-label="Client portrait"></div>
    <div class="quote-mark">&#8220;</div>
    <p>Sed ut perspiciatis unde omnis iste natus error sit voluptatem accusantium dol ompue la ntuperiam, eaae</p>
    <div class="quote-mark" style="margin-top:16px">&#8221;</div>
    <div class="name">Arjun Mehta</div>
  </div>

  <div class="abs dots" style="top:583px"><i></i><i></i></div>
</section>

<section class="cta">
  <h2 class="abs cta-title">Get free<span class="bar"></span><span class="thin">Consultation</span></h2>
  <p class="abs cta-copy">Lorem ipsum dolor sit amet, consectetur adipiscing elit, sed do eiusmod tempor incididunt ut labore</p>
  <div class="abs btn-white">CLICK HERE</div>
</section>

<footer class="site-footer">
  <div class="abs skyline" role="img" aria-label="Faded city skyline"></div>
  <svg class="abs" style="left:330px;top:98px" width="26" height="34" viewBox="0 0 26 34" fill="none" stroke="#f26a12" stroke-width="2">
    <path d="M13 32S2 19 2 12a11 11 0 0122 0c0 7-11 20-11 20z"/><circle cx="13" cy="12" r="4"/>
  </svg>
  <div class="abs f-name">PVT Law Group PLLC</div>
  <div class="abs f-addr">PVT LAW GROUP PLLC<br>2240 Harbor Lane North, Suite 300<br>Seattle, WA 98121</div>
  <div class="abs f-divider"></div>
  <svg class="abs" style="left:633px;top:100px" width="24" height="24" viewBox="0 0 24 24" fill="none" stroke="#f26a12" stroke-width="2">
    <path d="M5 2h4l2 5-3 2a12 12 0 006 6l2-3 5 2v4a2 2 0 01-2 2A18 18 0 013 4a2 2 0 012-2z"/>
  </svg>
  <div class="abs f-phone">206.555.0143<br>206.555.0144</div>
  <svg class="abs" style="left:634px;top:187px" width="22" height="20" viewBox="0 0 22 20" fill="none" stroke="#f26a12" stroke-width="2">
    <path d="M2 8l9-6 9 6v10H2z"/><path d="M2 8l9 6 9-6"/>
  </svg>
  <div class="abs f-mail">contact@pvtlawgroup.com</div>
  <div class="abs f-rule"></div>
  <nav class="abs social-links f-social" aria-label="Social links">
    <a href="#">Share</a><span class="sep"></span><a href="#">Post</a><span class="sep"></span><a href="#">Plus</a><span class="sep"></span><a href="#">Connect</a>
  </nav>
  <div class="abs copyright">Copyright © PVT Law Group PLLC 2017</div>
  <svg class="abs to-top" viewBox="0 0 32 32" fill="none" stroke="#333" stroke-width="1.5"><path d="M10 19l6-6 6 6"/></svg>
</footer>

</body>
</html>
```